We need a template newsletter design for our quarterly newsletter that we issue to employees. The newsletter generally holds updates from different departments such as:

CEO
Finance
Operations
Human Resources, ETC
(Please allow the pages to be copied)

I am looking for a template that has headings on each page, text space and image space. I am looking for a funky hip design with some great colour and creative imagination.

If you could create a cover page that includes the name "Harbourlinks" and the edition "Month, Year".

There is no requirements for specific logos or colours to be incorporated into this newsletter.

If possible I would like each page to have a different layout/design but for it to still flow as one newsletter. (Work with 4 pages/headings as listed above)

The document must be produced in InDesign.

Reason: Hi Guys, Whilst I love the designs submitted I am looking for a less formal and more creative funky design. Project is extended another 2 days. Thank you Merv

```html
<!DOCTYPE html>
<html lang="en">
<head>
<meta charset="utf-8">
<title>Harbourlinks – Edition 01</title>
<link rel="stylesheet" href="https://fonts.googleapis.com/css2?family=Open+Sans:wght@600;700&family=PT+Sans:ital,wght@0,400;0,700;1,700&family=PT+Sans+Narrow:wght@700&display=swap">
<style>
  :root {
    --backdrop: #5e5e5e;
    --paper: #ffffff;
    --ink: #3a3a3a;
    --ink-soft: #555555;
    --masthead: #666666;
    --accent: #11a6e3;
    --caption-bg: #e4e4e4;
    --photo-light: #e9eef2;
    --photo-mid: #c9d2da;
    --photo-dark: #6f7780;
  }
  * { box-sizing: border-box; margin: 0; padding: 0; }
  html, body {
    width: 909px; height: 1200px; overflow: hidden;
    background: var(--backdrop);
  }
  .page {
    position: absolute; left: 72px; top: 60px;
    width: 764px; height: 1078px;
    background: var(--paper);
    font-family: "PT Sans", Arial, sans-serif;
    color: var(--ink);
  }
  .edition {
    position: absolute; left: 73px; top: 55px;
    font-family: "Open Sans", Arial, sans-serif;
    font-weight: 700; font-size: 14px; color: var(--ink);
    display: flex; align-items: center; gap: 6px;
  }
  .edition .bar { width: 3px; height: 13px; background: var(--accent); display: inline-block; }
  .masthead {
    position: absolute; left: 66px; top: 76px;
    font-family: "Open Sans", Arial, sans-serif;
    font-weight: 700; font-size: 97px; letter-spacing: -3.5px;
    line-height: 1.15; color: var(--masthead);
  }
  .masthead-rule {
    position: absolute; left: 73px; top: 195px;
    width: 618px; height: 2px; background: var(--ink);
  }
  .lead-photo {
    position: absolute; left: 73px; top: 219px;
    width: 617px; height: 268px;
    background: linear-gradient(100deg, var(--photo-light) 0%, var(--photo-mid) 45%, var(--photo-dark) 70%, var(--photo-light) 100%);
  }
  .headline {
    position: absolute; left: 73px; top: 508px;
    font-family: "PT Sans Narrow", "Arial Narrow", sans-serif;
    font-weight: 700; font-size: 57px; line-height: 1.1;
    color: var(--accent); letter-spacing: -0.5px;
  }
  .standfirst {
    position: absolute; left: 73px; top: 582px; width: 620px;
    font-weight: 700; font-size: 15.2px; line-height: 19px;
    color: var(--ink-soft);
  }
  .column {
    position: absolute; top: 660px; width: 192px; height: 325px;
    overflow: hidden;
    font-size: 11.2px; line-height: 14.2px;
    text-align: justify; hyphens: none;
  }
  .column p { margin-bottom: 14.2px; }
  .column p.tight { margin-bottom: 0; }
  .column .pull { color: var(--accent); font-weight: 700; }
  .column-one { left: 73px; }
  .column-two { left: 286px; }
  .feature-card {
    position: absolute; left: 502px; top: 662px; width: 189px; height: 326px;
    background: var(--caption-bg);
  }
  .feature-photo {
    width: 189px; height: 158px;
    background: linear-gradient(90deg, #b9c3cc 0%, #8a96a2 45%, #d8e3ec 100%);
  }
  .feature-quote {
    padding: 12px 16px 0 18px;
    font-style: italic; font-weight: 700; font-size: 13.1px; line-height: 16.5px;
    color: var(--ink);
  }
  .feature-credit {
    position: absolute; right: 12px; bottom: 10px;
    font-style: italic; font-weight: 700; font-size: 10.5px; color: var(--accent);
  }
  .site-address {
    position: absolute; right: 72px; top: 1011px;
    font-size: 13px; color: var(--ink);
  }
</style>
</head>
<body>
<main class="page">
  <div class="edition"><span class="bar"></span>Edition : 01<span class="bar"></span>September 2016</div>
  <h1 class="masthead">Harbourlinks</h1>
  <div class="masthead-rule"></div>

  <div class="lead-photo" role="img" aria-label="Photo of three contact centre staff with headsets looking at a screen"></div>

  <h2 class="headline">Delivering award-winning</h2>
  <p class="standfirst">Delivering award-winning, innovative customer experience management solutions and invaluable customer insights Delivering award-winning, innovative custo Delivering award-winning, innovative customer experience management solutions</p>

  <section class="column column-one">
    <p>From strategy design to consulting on the customer experience, to implementation of new services and the evolution of existing contact centre operations, we’re the industry leading partners for contact centres outsourcing across Australia.</p>
    <p class="pull">Every client’s needs are different. Some want to touch and feel their solution, so we offer operations from coast to coast in Australia.</p>
    <p>Others are looking for a way to deliver exceptional results for a lower cost, so we offer two call centres in the Philippines – a global customer experience presence we’ve been carefully developing since 2007. From strategy design to consulting on the customer experience, to implementation of new services and the evolution of existing contact centre operations, we’re</p>
  </section>

  <section class="column column-two">
    <p>Every client’s needs are different. Some want to touch and feel their solution, so we offer operations from coast to coast in Australia.</p>
    <p>Others are looking for a way to deliver exceptional results for a lower cost, so we offer two call centres in the Philippines – a global customer experience presence we’ve been carefully developing since 2007. From strategy design to consulting on the customer experience, to implementation of new services and the evolution of existing contact centre operations, we’re the industry leading partners for contact centres outsourcing across Australia.</p>
    <p class="tight">Every client’s needs are different. Some want to touch and feel their solution, so we offer operations from coast to coast in Australia.</p>
    <p>Others are looking for a way to deliver</p>
  </section>

  <aside class="feature-card">
    <div class="feature-photo" role="img" aria-label="Photo of a smiling team member giving a thumbs up in an office"></div>
    <p class="feature-quote">From strategy design to consulting on the customer experience, to implementation of new services and the evolution of existing contact centre operations, we’re the</p>
    <p class="feature-credit">From strategy design t</p>
  </aside>

  <p class="site-address">www.harbourlinksnews.com.au</p>
</main>
</body>
</html>
```